Company Profile

I need each page contain text and images, the image have to be related to the text and our activity (fruits and vegetables trading ).

2 cover pages and 4 pages inside (8 faces). the back cover has to contain a pocket to save the A4 quotations and place to hold the salesman business card.
I do not have the logo source, so you need to redraw it again and feel free to make any changes to the logo.

This link contain , logo and brochure text. https://files.trelvanshare.net/u/90317254/merquata.zip

```html
<!DOCTYPE html>
<html lang="en">
<head>
<meta charset="utf-8">
<title>Merquata – Company Profile Folder Covers</title>
<link rel="stylesheet" href="https://fonts.googleapis.com/css2?family=Open+Sans:wght@400;600;700&display=swap">
<style>
  :root {
    --backdrop: #d9d9d9;
    --lime: #a8cc3a;
    --lime-deep: #8fb52a;
    --leaf-green: #1f8a3a;
    --text-green: #2a8a2e;
    --maroon: #9e1b2b;
    --paper-white: #ffffff;
    --paper-grey: #e4e4e4;
    --tagline-grey: #6a6a6a;
  }
  * { margin: 0; padding: 0; box-sizing: border-box; }
  html, body {
    width: 1200px;
    height: 800px;
    overflow: hidden;
    background: var(--backdrop);
    font-family: "Open Sans", Arial, sans-serif;
  }
  .folder-spread {
    position: absolute;
    left: 210px;
    top: 110px;
    width: 780px;
    height: 580px;
    box-shadow: 0 10px 30px rgba(0,0,0,0.18);
  }
  .folder-spread svg { display: block; }
  .back-cover-contact {
    position: absolute;
    left: 30px;
    top: 480px;
    color: var(--text-green);
    font-size: 9px;
    line-height: 10.5px;
  }
  .back-cover-contact p { margin-bottom: 12px; }
  .back-cover-contact strong { font-weight: 700; }
  .front-cover-brand {
    position: absolute;
    left: 590px;
    top: 66px;
    width: 170px;
    text-align: right;
  }
  .brand-name {
    color: var(--leaf-green);
    font-size: 34px;
    font-weight: 700;
    line-height: 44px;
  }
  .brand-tagline {
    color: var(--tagline-grey);
    font-size: 8.5px;
    letter-spacing: 0.2px;
    text-transform: uppercase;
    margin-top: 12px;
  }
</style>
</head>
<body>
  <main class="folder-spread">
    <svg width="780" height="580" viewBox="0 0 780 580">
      <defs>
        <linearGradient id="backCoverPaper" x1="0" y1="0" x2="0.6" y2="1">
          <stop offset="0" stop-color="var(--paper-white)"/>
          <stop offset="0.35" stop-color="#e6f2b8"/>
          <stop offset="1" stop-color="var(--lime)"/>
        </linearGradient>
        <linearGradient id="frontCoverPaper" x1="1" y1="0" x2="0.3" y2="1">
          <stop offset="0" stop-color="var(--paper-grey)"/>
          <stop offset="0.45" stop-color="#cfdca0"/>
          <stop offset="1" stop-color="var(--lime-deep)"/>
        </linearGradient>

        <linearGradient id="vegetableBase" x1="0" y1="0" x2="0.4" y2="1">
          <stop offset="0" stop-color="#3f7a25"/>
          <stop offset="0.5" stop-color="#7a4a30"/>
          <stop offset="1" stop-color="#5f8f2c"/>
        </linearGradient>
        <radialGradient id="vegGreens" cx="0.5" cy="0.5" r="0.5">
          <stop offset="0" stop-color="#4e9a2c" stop-opacity="0.95"/>
          <stop offset="1" stop-color="#4e9a2c" stop-opacity="0"/>
        </radialGradient>
        <radialGradient id="vegCream" cx="0.5" cy="0.5" r="0.5">
          <stop offset="0" stop-color="#efe9d6" stop-opacity="0.95"/>
          <stop offset="1" stop-color="#efe9d6" stop-opacity="0"/>
        </radialGradient>
        <radialGradient id="vegRed" cx="0.5" cy="0.5" r="0.5">
          <stop offset="0" stop-color="#c9201f" stop-opacity="0.95"/>
          <stop offset="1" stop-color="#c9201f" stop-opacity="0"/>
        </radialGradient>
        <radialGradient id="vegBeet" cx="0.5" cy="0.5" r="0.5">
          <stop offset="0" stop-color="#8a2a45" stop-opacity="0.9"/>
          <stop offset="1" stop-color="#8a2a45" stop-opacity="0"/>
        </radialGradient>
        <radialGradient id="vegYellow" cx="0.5" cy="0.5" r="0.5">
          <stop offset="0" stop-color="#f1d24a" stop-opacity="0.95"/>
          <stop offset="1" stop-color="#f1d24a" stop-opacity="0"/>
        </radialGradient>

        <linearGradient id="fruitBase" x1="0" y1="0" x2="0.5" y2="1">
          <stop offset="0" stop-color="#b8623a"/>
          <stop offset="0.5" stop-color="#a8683f"/>
          <stop offset="1" stop-color="#c9503a"/>
        </linearGradient>
        <radialGradient id="fruitOrange" cx="0.5" cy="0.5" r="0.5">
          <stop offset="0" stop-color="#f58a12" stop-opacity="0.95"/>
          <stop offset="1" stop-color="#f58a12" stop-opacity="0"/>
        </radialGradient>
        <radialGradient id="fruitPeach" cx="0.5" cy="0.5" r="0.5">
          <stop offset="0" stop-color="#e59a7c" stop-opacity="0.95"/>
          <stop offset="1" stop-color="#e59a7c" stop-opacity="0"/>
        </radialGradient>
        <radialGradient id="fruitGrape" cx="0.5" cy="0.5" r="0.5">
          <stop offset="0" stop-color="#a9c24a" stop-opacity="0.95"/>
          <stop offset="1" stop-color="#a9c24a" stop-opacity="0"/>
        </radialGradient>
        <radialGradient id="fruitBrown" cx="0.5" cy="0.5" r="0.5">
          <stop offset="0" stop-color="#9a6a42" stop-opacity="0.95"/>
          <stop offset="1" stop-color="#9a6a42" stop-opacity="0"/>
        </radialGradient>
        <radialGradient id="fruitLemon" cx="0.5" cy="0.5" r="0.5">
          <stop offset="0" stop-color="#efe07a" stop-opacity="0.95"/>
          <stop offset="1" stop-color="#efe07a" stop-opacity="0"/>
        </radialGradient>
        <radialGradient id="fruitRed" cx="0.5" cy="0.5" r="0.5">
          <stop offset="0" stop-color="#d8333a" stop-opacity="0.9"/>
          <stop offset="1" stop-color="#d8333a" stop-opacity="0"/>
        </radialGradient>

        <clipPath id="produceWindow">
          <path d="M170,380 A220,220 0 0 1 610,380 C610,430 560,450 535,500 C515,540 514,565 516,580 L264,580 C266,565 265,540 245,500 C220,450 170,430 170,380 Z"/>
        </clipPath>
        <clipPath id="leftHalf"><rect x="0" y="0" width="390" height="580"/></clipPath>
        <clipPath id="rightHalf"><rect x="390" y="0" width="390" height="580"/></clipPath>
      </defs>

      <rect class="back-cover" x="0" y="0" width="390" height="580" fill="url(#backCoverPaper)"/>
      <rect class="front-cover" x="390" y="0" width="390" height="580" fill="url(#frontCoverPaper)"/>

      <g clip-path="url(#produceWindow)">
        <g class="vegetable-photo" clip-path="url(#leftHalf)" role="img"
           aria-label="Photo of fresh vegetables: cauliflower, beetroot, tomatoes, peppers, cucumber, corn and greens">
          <rect x="0" y="0" width="390" height="580" fill="url(#vegetableBase)"/>
          <ellipse cx="320" cy="200" rx="90" ry="70" fill="url(#vegGreens)"/>
          <ellipse cx="240" cy="300" rx="75" ry="70" fill="url(#vegCream)"/>
          <ellipse cx="330" cy="330" rx="70" ry="80" fill="url(#vegBeet)"/>
          <ellipse cx="200" cy="420" rx="65" ry="60" fill="url(#vegRed)"/>
          <ellipse cx="290" cy="400" rx="55" ry="50" fill="url(#vegRed)"/>
          <ellipse cx="340" cy="460" rx="60" ry="45" fill="url(#vegGreens)"/>
          <ellipse cx="330" cy="540" rx="90" ry="45" fill="url(#vegYellow)"/>
        </g>
        <g class="fruit-photo" clip-path="url(#rightHalf)" role="img"
           aria-label="Photo of fresh fruits: oranges, peaches, grapes, coconut, pomegranate, lemons and watermelon">
          <rect x="390" y="0" width="390" height="580" fill="url(#fruitBase)"/>
          <ellipse cx="500" cy="200" rx="80" ry="45" fill="url(#fruitGrape)"/>
          <ellipse cx="420" cy="240" rx="50" ry="45" fill="url(#fruitOrange)"/>
          <ellipse cx="500" cy="280" rx="55" ry="55" fill="url(#fruitPeach)"/>
          <ellipse cx="565" cy="310" rx="50" ry="45" fill="url(#fruitOrange)"/>
          <ellipse cx="450" cy="390" rx="70" ry="60" fill="url(#fruitBrown)"/>
          <ellipse cx="570" cy="380" rx="50" ry="55" fill="url(#fruitLemon)"/>
          <ellipse cx="530" cy="440" rx="45" ry="40" fill="url(#fruitRed)"/>
          <ellipse cx="420" cy="490" rx="45" ry="55" fill="url(#fruitRed)"/>
          <ellipse cx="500" cy="520" rx="60" ry="55" fill="url(#fruitPeach)"/>
        </g>
      </g>

      <path class="window-frame-green" clip-path="url(#leftHalf)" fill="none" stroke="var(--leaf-green)" stroke-width="4"
            d="M170,380 A220,220 0 0 1 610,380 C610,430 560,450 535,500 C515,540 514,565 516,580 M264,580 C266,565 265,540 245,500 C220,450 170,430 170,380"/>
      <path class="window-frame-maroon" clip-path="url(#rightHalf)" fill="none" stroke="var(--maroon)" stroke-width="4"
            d="M170,380 A220,220 0 0 1 610,380 C610,430 560,450 535,500 C515,540 514,565 516,580 M264,580 C266,565 265,540 245,500 C220,450 170,430 170,380"/>

      <line class="spine" x1="390" y1="0" x2="390" y2="580" stroke="rgba(0,0,0,0.08)" stroke-width="1"/>
    </svg>

    <section class="back-cover-contact">
      <p><strong>For your information<br>please contact us on</strong><br>info@merquata.com</p>
      <p><strong>For your order please contact us on</strong><br>
        <strong>Email</strong> sales@merquata.com<br>
        <strong>Tel</strong> +965-20417735 | <strong>Fax</strong> +965-20417736<br>
        <strong>www.merquata.com</strong></p>
    </section>

    <header class="front-cover-brand">
      <div class="brand-name">Merquata</div>
      <div class="brand-tagline">Healthy and Natural products</div>
    </header>
  </main>
</body>
</html>
```